Mardi Gras 2013 Design Project

We have a design with elements that we want to retain. However, we need to take what we have and give it a creative BOOST!

Requirements
Must have
• Colors must stay, "KT" logo must stay,
Copy must remain (except - "Requests Your Presence" and small copy in bottom right corner);
Seal must remain, "9th Annual Velvet Lantern Gala" frame text can be modified but should resemble;
Gotham font to remain
Nice to have
• Any new Mardi Gras element - like a mask or beads - but can not over shadow copy

```html
<!DOCTYPE html>
<html lang="en">
<head>
<meta charset="utf-8">
<title>9th Annual Velvet Lantern Gala</title>
<link rel="stylesheet" href="https://fonts.googleapis.com/css2?family=Montserrat:ital,wght@0,700;0,800;0,900;1,700;1,800;1,900&family=Roboto+Condensed:wght@400;700&display=swap">
<style>
  :root {
    --paper: #ffffff;
    --royal: #4f3590;
    --gold: #efb33c;
    --green: #3dae4a;
    --lilac: #7b5cab;
    --lilac-text: #8f70c4;
    --deep: #2e1a5c;
  }
  * { margin: 0; padding: 0; box-sizing: border-box; }
  html, body { width: 1200px; height: 1000px; overflow: hidden; background: var(--paper); }
  body { position: relative; font-family: "Montserrat", Arial, sans-serif; }

  .panel { position: absolute; top: 148px; height: 732px; background: var(--royal); overflow: hidden; }
  .panel--invite { left: 12px; width: 584px; }
  .panel--cover { left: 608px; width: 580px; }

  .stripes { position: absolute; inset: 0; width: 584px; height: 732px; }

  .t { position: absolute; white-space: nowrap; line-height: 1; font-style: italic; font-weight: 800; }

  .monogram { position: absolute; left: 30px; top: 62px; font-weight: 900; font-size: 118px; color: var(--gold); line-height: 1; letter-spacing: -2px; }

  .host { left: 296px; top: 56px; color: var(--gold); line-height: 1.35; }
  .host-line1 { display: block; font-size: 15px; letter-spacing: 1px; }
  .host-line2 { display: block; font-size: 12.5px; letter-spacing: 0.3px; }
  .request-top { left: 358px; top: 122px; font-size: 11px; color: var(--gold); font-style: normal; line-height: 1.15; }

  .outline {
    font-weight: 900;
    color: var(--royal);
    --ol: var(--gold);
    text-shadow:
      1px 0 0 var(--ol), -1px 0 0 var(--ol), 0 1px 0 var(--ol), 0 -1px 0 var(--ol),
      1px 1px 0 var(--ol), -1px -1px 0 var(--ol), 1px -1px 0 var(--ol), -1px 1px 0 var(--ol);
  }
  .title-num { left: 268px; top: 142px; font-size: 108px; --ol: var(--green); letter-spacing: -4px; }
  .title-annual { left: 243px; top: 250px; font-size: 40px; --ol: var(--gold); }
  .title-a { left: 204px; top: 290px; font-size: 46px; --ol: var(--lilac-text); }
  .title-b { left: 210px; top: 341px; font-size: 46px; --ol: var(--green); }
  .title-c { left: 238px; top: 392px; font-size: 46px; --ol: var(--gold); }

  .seal { position: absolute; left: 122px; top: 376px; width: 90px; height: 90px; border-radius: 50%; background: var(--gold); display: flex; align-items: center; justify-content: center; }
  .seal-name { font-weight: 800; font-size: 11px; color: var(--deep); text-align: center; line-height: 1.2; }

  .day { left: 198px; top: 458px; font-size: 26px; color: var(--gold); }
  .date { left: 160px; top: 494px; font-size: 20px; color: var(--green); }
  .time { left: 162px; top: 526px; font-size: 20px; color: var(--lilac-text); }
  .at { left: 192px; top: 556px; font-size: 20px; color: var(--lilac-text); }
  .venue { left: 122px; top: 596px; font-size: 14px; color: var(--gold); line-height: 1.55; }
  .address { left: 102px; top: 652px; font-size: 14px; color: var(--green); font-style: normal; font-family: "Roboto Condensed", Arial, sans-serif; font-weight: 700; }
  .city { left: 94px; top: 672px; font-size: 17px; color: var(--green); }
  .request-bottom { left: 92px; top: 702px; font-size: 11px; color: var(--gold); }

  .details { position: absolute; right: 20px; top: 606px; text-align: right; color: var(--gold); font-family: "Roboto Condensed", Arial, sans-serif; line-height: 1.3; }
  .details .cost { font-family: "Montserrat", Arial, sans-serif; font-style: italic; font-weight: 800; font-size: 12px; margin-bottom: 8px; }
  .details .dress-title { font-weight: 700; font-size: 14px; }
  .details .dress-line { font-size: 11px; }

  .cover-mark { position: absolute; inset: 0; display: flex; align-items: center; justify-content: center; font-weight: 900; font-size: 330px; color: var(--gold); letter-spacing: -10px; line-height: 1; }
</style>
</head>
<body>
  <section class="panel panel--invite" aria-label="Gala invitation">
    <svg class="stripes" viewBox="0 0 584 732" aria-hidden="true">
      <polygon points="302,0 316,0 224,282 210,282" fill="var(--lilac)"/>
      <polygon points="530,0 544,0 464,252 450,252" fill="var(--gold)"/>
      <rect x="0" y="320" width="228" height="10" fill="var(--gold)"/>
      <polygon points="192,337 206,337 76,732 62,732" fill="var(--green)"/>
      <rect x="418" y="430" width="166" height="10" fill="var(--green)"/>
      <polygon points="380,447 394,447 294,732 280,732" fill="var(--lilac)"/>
    </svg>

    <div class="monogram">KT</div>

    <p class="t host"><span class="host-line1">THE &nbsp;ASSOCIATION &nbsp;OF</span><span class="host-line2">KINGSLEY TERRACE ALUMNI</span></p>
    <p class="t request-top">REQUESTS<br>YOUR PRESENCE<br>AT OUR</p>

    <h1>
      <span class="t outline title-num">9th</span>
      <span class="t outline title-annual">ANNUAL</span>
      <span class="t outline title-a">VELVET</span>
      <span class="t outline title-b">LANTERN</span>
      <span class="t outline title-c">GALA</span>
    </h1>

    <div class="seal"><span class="seal-name">Kingsley<br>Terrace</span></div>

    <p class="t day">SATURDAY</p>
    <p class="t date">JANUARY 26, 2013</p>
    <p class="t time">7 PM TO 12 AM</p>
    <p class="t at">AT THE</p>
    <p class="t venue">HARBORVIEW CIVIC<br>CONFERENCE CENTER</p>
    <p class="t address">1450 Meridian Hall Concourse</p>
    <p class="t city">RIVERTON, GEORGIA</p>
    <p class="t request-bottom">REQUESTS YOUR PRESENCE</p>

    <div class="details">
      <p class="cost">Cost: $75.00</p>
      <p class="dress-title">A Semi Formal Affair</p>
      <p class="dress-line">Tuxedos, Dark Suits and Ties</p>
      <p class="dress-line">NO HATS ALLOWED</p>
      <p class="dress-line">Tea Length or Formal Dresses</p>
    </div>
  </section>

  <section class="panel panel--cover" aria-label="Invitation cover">
    <div class="cover-mark">KT</div>
  </section>
</body>
</html>
```